Business card design for Allied Healthcare provider

We would like a design for front and back of business cards. The design must resonate with all levels of customers from patients, to other health providers and medical. Must also resonate with corporate customers

Target Market(s)

patients, medical practitioners, other health providers and corporate.

Industry/Entity Type

healthcare

Contact Information for Business Card

name, logo, phone and fax numbers, email, website

Requirements
Must have
• not allowing me to change this, but the card must be double sided!! Please take note
Nice to have
• a fresh yet bold design to catch attention.

```html
<!DOCTYPE html>
<html lang="en">
<head>
<meta charset="utf-8">
<title>Corvenhealth business card – front and back</title>
<link rel="stylesheet" href="https://fonts.googleapis.com/css2?family=Poppins:wght@400;600;700&family=Roboto:wght@400;500&display=swap">
<style>
  :root{
    --stage:#2a2a2c;
    --navy:#1b2a56;
    --navy-deep:#16234a;
    --navy-soft:#22336a;
    --gold:#fbb41c;
    --white:#ffffff;
  }
  *{box-sizing:border-box;margin:0;padding:0}
  html,body{width:1200px;height:900px;overflow:hidden;background:var(--stage)}
  .canvas{width:1200px;height:900px;display:flex;flex-direction:column;align-items:center;justify-content:center;gap:40px}
  .card{width:700px;height:400px;background:var(--navy);position:relative;overflow:hidden;box-shadow:0 12px 30px rgba(0,0,0,.45)}

  /* front */
  .card-front .gold-band{position:absolute;left:0;right:0;bottom:0;height:12px;background:var(--gold)}
  .brand{position:absolute;left:70px;top:150px;display:flex;flex-direction:column}
  .brand-name{display:flex;align-items:center;gap:12px;font-family:"Poppins",sans-serif;font-weight:600;font-size:40px;color:var(--white);letter-spacing:.5px;line-height:1}
  .brand-dot{width:22px;height:22px;border-radius:50%;background:var(--gold)}
  .brand-tagline{margin-top:8px;margin-left:34px;font-family:"Poppins",sans-serif;font-size:14px;color:var(--gold);letter-spacing:.5px}
  .divider{position:absolute;left:392px;top:110px;width:1px;height:180px;background:var(--gold);opacity:.8}
  .person{position:absolute;left:420px;top:122px;color:var(--white)}
  .person-name{font-family:"Poppins",sans-serif;font-weight:700;font-size:26px;color:var(--gold);text-transform:uppercase;line-height:1.1}
  .person-title{font-family:"Roboto",sans-serif;font-size:15px;margin-top:2px}
  .contact-list{list-style:none;margin-top:16px;font-family:"Roboto",sans-serif;font-size:15px;line-height:1.65}
  .contact-list li{display:flex;align-items:center;gap:9px}
  .contact-list svg{width:13px;height:13px;flex:none;fill:var(--gold)}

  /* back */
  .card-back .pattern{position:absolute;inset:0;background:linear-gradient(135deg,var(--navy-deep),var(--navy) 55%,var(--navy-soft))}
  .back-brand{position:absolute;right:40px;bottom:34px;display:flex;align-items:center;gap:8px;font-family:"Poppins",sans-serif;font-weight:600;font-size:18px;color:var(--white)}
  .back-brand .brand-dot{width:12px;height:12px}
</style>
</head>
<body>
<main class="canvas">
  <section class="card card-front" aria-label="Card front">
    <div class="brand">
      <div class="brand-name"><span class="brand-dot"></span>corvenhealth</div>
      <div class="brand-tagline">healing · care · wellbeing</div>
    </div>
    <div class="divider"></div>
    <div class="person">
      <h1 class="person-name">Daniel Hart</h1>
      <p class="person-title">CEO/Founder</p>
      <ul class="contact-list">
        <li><svg viewBox="0 0 16 16"><path d="M3.5 1l2.5 3-1.5 1.8c.9 1.9 2.4 3.4 4.2 4.2L10.5 8.5l3 2.5-1.5 3C6.5 14 2 9.5 2 3.9z"/></svg>(02) 5550 1846</li>
        <li><svg viewBox="0 0 16 16"><path d="M4 1h6l2 2v3H4zM2 7h12v6h-2v2H4v-2H2zm3 4v3h6v-3z"/></svg>(02) 5550 1872</li>
        <li><svg viewBox="0 0 16 16"><path d="M1 3h14v10H1zm1.5 1.2v.4L8 9l5.5-4.4v-.4z"/></svg>info@corvenhealth.com</li>
        <li><svg viewBox="0 0 16 16"><path d="M8 1a7 7 0 100 14A7 7 0 008 1zm0 1.5c.9 0 1.9 1.8 2.2 4.5H5.8C6.1 4.3 7.1 2.5 8 2.5zM2.6 7h1.8a13 13 0 000 2H2.6a5.5 5.5 0 010-2zm9 0h1.8a5.5 5.5 0 010 2h-1.8a13 13 0 000-2zM5.8 9h4.4c-.3 2.7-1.3 4.5-2.2 4.5S6.1 11.7 5.8 9z"/></svg>www.corvenhealth.com</li>
      </ul>
    </div>
    <div class="gold-band"></div>
  </section>

  <section class="card card-back" aria-label="Card back">
    <div class="pattern" role="img" aria-label="Tonal embossed brand pattern on navy"></div>
    <div class="back-brand"><span class="brand-dot"></span>corvenhealth</div>
  </section>
</main>
</body>
</html>
```